Design a refer a friend Flyer (French & English)
Flyer Title:
Main Title: "Refer a Friend & Receive a Free Electric Toothbrush!"
Bold and clear, centered at the top.
Use a clean and modern font.
Color: White text on a vivid green background for maximum contrast and readability.
Visual Focus:
Toothbrush Image: Place a high-quality image of the Dentiva Glide 300 Electric Toothbrush in the center of the flyer.
Include a small price tag with “Value of $50” near the toothbrush to highlight the reward.
Simple Message:
Text: "Refer a friend to Centre Dentaire Val-Fleuri. When they book and attend their appointment, you get a free electric toothbrush, and they receive a special gift!"
Straightforward and easy to understand.
Placed below the image of the toothbrush.
Referral Process:
3 Easy Steps:
Refer a Friend
They Book and Come to Their Appointment
Receive Your Free Electric Toothbrush
Use simple, minimal icons to visually represent each step.
Keep the steps aligned horizontally or vertically for clarity.
Call to Action:
Text: "Start Referring Today!"
Place it in a button-like design in the vivid green color with bold, white text to make it stand out.
Contact Information:
Details:
Logo of Centre Dentaire Val-Fleuri.
Address: "48 Rue Lambert Ouest, Suite 210".
Phone Number and Website: Positioned at the bottom for easy reference.
Color Scheme:
Use a vivid green background for the entire flyer, with white accents for text and icons to maintain a fresh, clean look.
Minimal clutter, focusing on clarity and the key elements: the toothbrush, the call to action, and contact information.
Clinic : www.cdvalfleuri-example.com
Attached is the brandbook, logo and inspo I made with AI.
French text will be provided.
Thank you,
Idris

```html
<!DOCTYPE html>
<html lang="en">
<head>
<meta charset="utf-8">
<title>Refer a Friend Flyer – Clinique Dentaire Val-Fleuri</title>
<link href="https://fonts.googleapis.com/css2?family=Archivo+Black&family=Lexend:wght@300;500;600;700&display=swap" rel="stylesheet">
<style>
  :root {
    --green: #00ad4f;
    --white: #ffffff;
    --paper: #f1f1f1;
    --page-bg: #dfe6e6;
    --brush-blue: #3d7fd6;
    --brush-light: #7fb5ea;
  }
  * { margin: 0; padding: 0; box-sizing: border-box; }
  html, body { width: 1200px; height: 1117px; overflow: hidden; background: var(--page-bg); }
  .flyer {
    position: absolute; left: 220px; top: 20px;
    width: 760px; height: 1077px;
    background: var(--green); color: var(--white);
    font-family: "Lexend", sans-serif;
    overflow: hidden;
  }
  .abs { position: absolute; }
  .headline {
    left: 0; right: 0; top: 50px; text-align: center;
    font-family: "Archivo Black", sans-serif; font-size: 36px; line-height: 43px;
    letter-spacing: 0.2px; text-transform: uppercase;
  }
  .value-badge {
    left: 62px; top: 154px; width: 252px; height: 252px; border-radius: 50%;
    background: radial-gradient(circle at 40% 40%, #ffffff, var(--paper));
    color: var(--green); box-shadow: 4px 8px 14px rgba(0,0,0,.15);
  }
  .value-badge .label {
    position: absolute; left: 42px; top: 64px; width: 100px; text-align: center;
    font-family: "Archivo Black", sans-serif; font-size: 22px; line-height: 23px;
    text-transform: uppercase;
  }
  .value-badge .amount {
    position: absolute; left: 32px; top: 110px;
    font-family: "Archivo Black", sans-serif; font-size: 86px; line-height: 90px; letter-spacing: -3px;
  }
  .offer-text {
    left: 50px; width: 250px; top: 436px; text-align: center;
    font-weight: 500; font-size: 20px; line-height: 22.5px;
  }
  .offer-tagline {
    left: 34px; width: 282px; top: 632px; text-align: center;
    font-weight: 700; font-size: 27px; line-height: 30px;
  }
  .tooth-art {
    left: 113px; top: 756px; width: 142px; height: 144px; border-radius: 40px 40px 20px 20px;
    background: rgba(255,255,255,.9);
  }
  .product-photo {
    left: 316px; top: 142px; width: 152px; height: 772px; border-radius: 70px 70px 20px 20px;
    background: linear-gradient(180deg, #f4f6f8 0%, #f4f6f8 32%, var(--brush-light) 40%, var(--brush-blue) 70%, #f2f2f2 88%, #e8e8e8 100%);
  }
  .paste-art {
    left: 488px; top: 864px; width: 204px; height: 48px; border-radius: 24px;
    background: rgba(255,255,255,.9);
  }
  .steps-kicker { left: 470px; width: 244px; top: 178px; text-align: center; font-weight: 300; font-size: 17px; }
  .steps-title {
    left: 460px; width: 264px; top: 198px; text-align: center;
    font-family: "Archivo Black", sans-serif; font-size: 30px; line-height: 38px;
  }
  .step { left: 460px; width: 290px; height: 76px; }
  .step .ring {
    position: absolute; left: 9px; top: 0; width: 76px; height: 76px; border-radius: 50%;
    border: 3px solid var(--white);
  }
  .step .ring .core {
    position: absolute; left: 6px; top: 6px; width: 58px; height: 58px; border-radius: 50%;
    background: var(--white);
  }
  .step .ring svg { position: absolute; left: 13px; top: 13px; width: 44px; height: 44px; }
  .step .num {
    position: absolute; left: -3px; top: 26px; width: 24px; height: 24px; border-radius: 50%;
    background: var(--green); border: 2px solid var(--white);
    font-size: 14px; font-weight: 600; line-height: 20px; text-align: center;
  }
  .step .text {
    position: absolute; left: 100px; top: 50%; transform: translateY(-50%);
    font-weight: 600; font-size: 19px; line-height: 21.5px;
  }
  .cta {
    left: 476px; top: 538px; width: 234px; height: 29px; border-radius: 15px;
    background: var(--white); color: var(--green);
    font-weight: 700; font-size: 13.5px; line-height: 29px; text-align: center; letter-spacing: .2px;
  }
  .contact-card {
    left: 466px; top: 619px; width: 256px; height: 210px;
    border: 3px solid var(--white); border-radius: 18px;
  }
  .contact-card h2 {
    position: absolute; left: 22px; top: 18px; font-weight: 700; font-size: 24px; letter-spacing: .3px;
  }
  .contact-line {
    position: absolute; left: 22px; font-weight: 600; font-size: 15px; line-height: 19px;
    display: flex; gap: 8px; white-space: nowrap;
  }
  .contact-line svg { flex: none; width: 14px; height: 14px; margin-top: 3px; }
  .brand { left: 63px; top: 940px; }
  .brand .name { font-weight: 600; font-size: 58px; line-height: 66px; letter-spacing: -0.5px; }
  .brand .place { font-weight: 600; font-size: 25px; line-height: 30px; }
  .brand-dot { left: 612px; top: 948px; width: 72px; height: 72px; border-radius: 50%; background: var(--white); }
</style>
</head>
<body>
<main class="flyer">
  <h1 class="abs headline">Refer a Friend &amp; Receive a<br>Free Electric Toothbrush!</h1>

  <div class="abs value-badge">
    <div class="label">Value<br>of</div>
    <div class="amount">$50</div>
  </div>

  <p class="abs offer-text">Refer a friend to Centre Dentaire Val-Fleuri. When they book and attend their appointment, you get a free electric toothbrush, and they receive a special gift!</p>
  <p class="abs offer-tagline">Straightforward and easy to understand.</p>

  <div class="abs tooth-art" role="img" aria-label="White illustration of a tooth above a toothbrush"></div>

  <div class="abs product-photo" role="img" aria-label="Photo of the Dentiva Glide 300 electric toothbrush standing on its white charging base"></div>

  <div class="abs steps-kicker">Referral Process</div>
  <div class="abs steps-title">3 EASY STEPS</div>

  <div class="abs step" style="top:245px">
    <div class="ring"><div class="core"></div>
      <svg viewBox="0 0 44 44" aria-hidden="true"><g fill="#00ad4f"><circle cx="19" cy="14" r="7"/><path d="M6 36c0-8 6-13 13-13s10 3 11 6v7z"/><circle cx="32" cy="30" r="7" stroke="#fff" stroke-width="2"/></g><path d="M32 26v8M28 30h8" stroke="#fff" stroke-width="2"/></svg>
    </div>
    <div class="num">1</div>
    <div class="text">Refer a Friend</div>
  </div>

  <div class="abs step" style="top:330px">
    <div class="ring"><div class="core"></div>
      <svg viewBox="0 0 44 44" aria-hidden="true"><g fill="none" stroke="#00ad4f" stroke-width="3"><rect x="6" y="9" width="26" height="22" rx="2"/><line x1="6" y1="16" x2="32" y2="16"/><line x1="12" y1="5" x2="12" y2="11"/><line x1="26" y1="5" x2="26" y2="11"/><path d="M11 23l4 4 7-7"/></g></svg>
    </div>
    <div class="num">2</div>
    <div class="text">They Book and<br>Come to Their<br>Appointment</div>
  </div>

  <div class="abs step" style="top:416px">
    <div class="ring"><div class="core"></div>
      <svg viewBox="0 0 44 44" aria-hidden="true"><g fill="none" stroke="#00ad4f" stroke-width="3" stroke-linecap="round"><rect x="17" y="14" width="10" height="26" rx="4"/><line x1="22" y1="3" x2="22" y2="14"/><path d="M11 20c-3 4-3 8 0 12M33 20c3 4 3 8 0 12"/></g><circle cx="22" cy="22" r="2" fill="#00ad4f"/></svg>
    </div>
    <div class="num">3</div>
    <div class="text">Receive Your<br>Free Electric<br>Toothbrush</div>
  </div>

  <div class="abs cta">START REFERRING TODAY!</div>

  <section class="abs contact-card">
    <h2>CONTACT US</h2>
    <div class="contact-line" style="top:60px">
      <svg viewBox="0 0 14 14" aria-hidden="true"><circle cx="7" cy="7" r="7" fill="#fff"/><path d="M4.5 3.5l1.5 0 .6 2-1 .8a5 5 0 002.1 2.1l.8-1 2 .6v1.5c-3.5.5-7-3-6-6z" fill="#00ad4f"/></svg>
      <span>514-555-0182</span>
    </div>
    <div class="contact-line" style="top:102px">
      <svg viewBox="0 0 14 14" aria-hidden="true"><path d="M7 0a5 5 0 015 5c0 4-5 9-5 9S2 9 2 5a5 5 0 015-5z" fill="#fff"/><circle cx="7" cy="5" r="2" fill="#00ad4f"/></svg>
      <span>48 Rue Lambert Ouest,<br>Suite 210</span>
    </div>
    <div class="contact-line" style="top:164px">
      <svg viewBox="0 0 14 14" aria-hidden="true"><circle cx="7" cy="7" r="7" fill="#fff"/><g fill="none" stroke="#00ad4f" stroke-width="1"><ellipse cx="7" cy="7" rx="2.5" ry="5"/><line x1="2" y1="7" x2="12" y2="7"/></g></svg>
      <span>cdvalfleuri-example.com</span>
    </div>
  </section>

  <div class="abs paste-art" role="img" aria-label="White illustration of a toothpaste swirl"></div>

  <div class="abs brand">
    <div class="name">Clinique Dentaire</div>
    <div class="place">Val-Fleuri</div>
  </div>
  <div class="abs brand-dot"></div>
</main>
</body>
</html>
```